Boutique Real Estate Brokerage looking for business card, letterhead and envelope design

We are looking for a cohesive design for our business cards, letterhead and envelopes and that mirrors our high-end homes and clientele. Fern & Gable is being launched and designed for the marketplace of tomorrow. We grew from the #1 team in our community into a full-service firm that is going to revolutionize the traditional real estate model.

We understand that it’s more important than ever to help our clients and partners adapt to behavioral and market changes being driven by generational shifts and technological advances in society, and by combining traditional brokerage services with innovative production and marketing capabilities, we know how to do that better than anyone else.

Requirements
Must have
• business card, letterhead and envelope design - attached logo.

```html
<!DOCTYPE html>
<html lang="en">
<head>
<meta charset="utf-8">
<title>Fern &amp; Gable Realty – Stationery</title>
<link href="https://fonts.googleapis.com/css2?family=Poppins:wght@400;500;600;700&display=swap" rel="stylesheet">
<style>
  :root {
    --navy: #1a1060;
    --gold: #c08a4a;
    --backdrop: #8b8b8b;
    --paper: #ffffff;
    --grad-top: #c1874a;
    --grad-mid: #3b2168;
    --grad-bottom: #160a5a;
    --shadow: 0 3px 5px rgba(0,0,0,.35);
  }
  * { margin: 0; padding: 0; box-sizing: border-box; }
  html, body { width: 1200px; height: 1200px; overflow: hidden; }
  body { background: var(--backdrop); font-family: "Poppins", sans-serif; position: relative; color: var(--navy); }

  .sheet { position: absolute; background: var(--paper); box-shadow: var(--shadow); overflow: hidden; }

  .brand { display: flex; align-items: center; gap: 5px; white-space: nowrap; }
  .brand-mark { background: var(--gold); flex: none; }
  .brand-name { font-weight: 600; color: var(--navy); letter-spacing: .02em; line-height: 1; }
  .brand.on-dark .brand-name { color: #fff; }

  .contact { font-size: 5.4px; line-height: 8px; color: var(--navy); }
  .contact li { list-style: none; display: flex; align-items: center; gap: 3px; }
  .icon { width: 5px; height: 5px; flex: none; }
  .rule { height: 1px; }
  .rule.navy { background: var(--navy); }
  .rule.gold { background: var(--gold); }

  .band { position: absolute; left: 0; bottom: 0; width: 100%; }

  /* Letterhead */
  .letterhead { left: 91px; top: 268px; width: 466px; height: 659px; }
  .letterhead .brand { position: absolute; left: 25px; top: 27px; }
  .letterhead .brand-mark { width: 10px; height: 10px; }
  .letterhead .brand-name { font-size: 13px; }
  .letterhead .contact-block { position: absolute; right: 19px; top: 19px; width: 80px; text-align: right; }
  .letterhead .contact li { justify-content: flex-end; }
  .letterhead .address { margin-top: 8px; font-size: 5.4px; line-height: 8px; }
  .letterhead .rule.gold { width: 62px; margin: 5px 0 0 auto; }

  /* Business cards */
  .card-front { left: 576px; top: 268px; width: 265px; height: 156px; }
  .card-front .brand { position: absolute; left: 20px; top: 68px; gap: 4px; }
  .card-front .brand-mark { width: 6px; height: 6px; }
  .card-front .brand-name { font-size: 7px; }
  .card-front .divider { position: absolute; left: 143px; top: 38px; width: 1px; height: 75px; background: var(--gold); }
  .card-front .details { position: absolute; left: 153px; top: 37px; }
  .person-name { font-size: 7.5px; font-weight: 700; line-height: 9px; }
  .person-role { font-size: 5.6px; font-weight: 500; color: var(--gold); margin-bottom: 5px; }
  .card-front .address { margin-top: 4px; font-size: 5.4px; line-height: 8.5px; }

  .card-back { left: 850px; top: 268px; width: 265px; height: 156px;
    background: linear-gradient(180deg, var(--grad-top) 0%, var(--grad-mid) 50%, var(--grad-bottom) 100%); }
  .card-back .brand { position: absolute; left: 70px; top: 70px; }
  .card-back .brand-mark { width: 8px; height: 8px; }
  .card-back .brand-name { font-size: 11px; }

  /* Envelopes */
  .envelope-front { left: 576px; top: 442px; width: 540px; height: 229px; }
  .envelope-front .brand { position: absolute; left: 184px; top: 104px; }
  .envelope-front .brand-mark { width: 14px; height: 14px; }
  .envelope-front .brand-name { font-size: 17px; }

  .envelope-back { left: 576px; top: 695px; width: 538px; height: 228px; }
  .envelope-back .brand { position: absolute; left: 22px; top: 23px; }
  .envelope-back .brand-mark { width: 12px; height: 12px; }
  .envelope-back .brand-name { font-size: 17px; }
  .envelope-back .contact-block { position: absolute; left: 22px; top: 70px; width: 90px; }
  .envelope-back .rule.navy { width: 82px; margin-bottom: 5px; }
  .envelope-back .rule.gold { width: 63px; margin: 6px 0 6px; }
  .envelope-back .address { font-size: 5.4px; line-height: 8px; }
  .stamp-box { position: absolute; right: 22px; top: 18px; width: 57px; height: 63px; border: 1px solid #f1f1f4; }
</style>
</head>
<body>

<svg width="0" height="0" style="position:absolute">
  <defs>
    <symbol id="ico-phone" viewBox="0 0 10 10"><path d="M2 1l2 2-1 1.2c.6 1.3 1.5 2.2 2.8 2.8L7 6l2 2-1.3 1.3C4.5 9 1 5.5.7 2.3z" fill="#c08a4a"/></symbol>
    <symbol id="ico-mail" viewBox="0 0 10 10"><rect x="1" y="2" width="8" height="6" fill="#c08a4a"/><path d="M1 2l4 3 4-3" stroke="#fff" stroke-width=".8" fill="none"/></symbol>
    <symbol id="ico-web" viewBox="0 0 10 10"><circle cx="5" cy="5" r="4" fill="#c08a4a"/><path d="M1 5h8M5 1c-2 2.5-2 5.5 0 8M5 1c2 2.5 2 5.5 0 8" stroke="#fff" stroke-width=".6" fill="none"/></symbol>
  </defs>
</svg>

<!-- Letterhead -->
<section class="sheet letterhead">
  <div class="brand"><span class="brand-mark"></span><span class="brand-name">FERN &amp; GABLE REALTY</span></div>
  <div class="contact-block">
    <div class="rule navy"></div>
    <ul class="contact" style="margin-top:4px">
      <li>214 555 0148 <svg class="icon"><use href="#ico-phone"/></svg></li>
      <li>alex@fernandgable.com <svg class="icon"><use href="#ico-mail"/></svg></li>
      <li>www.fernandgable.com <svg class="icon"><use href="#ico-web"/></svg></li>
    </ul>
    <div class="rule gold"></div>
    <p class="address">180 Willow Street NE<br>Suite 300, Alder Falls<br>MI 49210</p>
  </div>
  <svg class="band" viewBox="0 0 466 9" height="9" preserveAspectRatio="none">
    <polygon points="0,0 231,0 238,9 0,9" fill="#c08a4a"/>
    <polygon points="234,0 466,0 466,9 241,9" fill="#1a1060"/>
  </svg>
</section>

<!-- Business card front -->
<section class="sheet card-front">
  <div class="brand"><span class="brand-mark"></span><span class="brand-name">FERN &amp; GABLE REALTY</span></div>
  <div class="divider"></div>
  <div class="details">
    <p class="person-name">ALEX ROWAN</p>
    <p class="person-role">MANAGING DIRECTOR</p>
    <ul class="contact">
      <li><svg class="icon"><use href="#ico-phone"/></svg> 214 555 0148</li>
      <li><svg class="icon"><use href="#ico-mail"/></svg> alex@fernandgable.com</li>
      <li><svg class="icon"><use href="#ico-web"/></svg> www.fernandgable.com</li>
    </ul>
    <p class="address">180 Willow Street NE<br>Suite 300, Alder Falls<br>MI 49210</p>
  </div>
  <svg class="band" viewBox="0 0 265 6" height="6" preserveAspectRatio="none">
    <polygon points="0,0 130,0 135,6 0,6" fill="#c08a4a"/>
    <polygon points="132,0 265,0 265,6 137,6" fill="#1a1060"/>
  </svg>
</section>

<!-- Business card back -->
<section class="sheet card-back">
  <div class="brand on-dark"><span class="brand-mark"></span><span class="brand-name">FERN &amp; GABLE REALTY</span></div>
</section>

<!-- Envelope front -->
<section class="sheet envelope-front">
  <div class="brand"><span class="brand-mark"></span><span class="brand-name">FERN &amp; GABLE REALTY</span></div>
</section>

<!-- Envelope back -->
<section class="sheet envelope-back">
  <div class="brand"><span class="brand-mark"></span><span class="brand-name">FERN &amp; GABLE REALTY</span></div>
  <div class="contact-block">
    <div class="rule navy"></div>
    <ul class="contact">
      <li><svg class="icon"><use href="#ico-phone"/></svg> 214 555 0148</li>
      <li><svg class="icon"><use href="#ico-mail"/></svg> alex@fernandgable.com</li>
      <li><svg class="icon"><use href="#ico-web"/></svg> www.fernandgable.com</li>
    </ul>
    <div class="rule gold"></div>
    <p class="address">180 Willow Street NE<br>Suite 300, Alder Falls<br>MI 49210</p>
  </div>
  <div class="stamp-box"></div>
</section>

</body>
</html>
```